Flyer für Tiertherapeutin
Eine sehr motivierte und kreative Designerin. Schon der erste Vorschlag war ganz nach meinen Vorstellungen.
Zielgruppe
Ich bin Tiertherapeutin für TCVM und Ernährungsberaterin für Hunde und Katzen. Mittels Akupunktur, Lasertherapie, Mykotherapie und Ernährungsberatung kommt es zu einer Linderung vorhandener Schmerzen, eine verbesserte Regulation der Organe und einer Steigerung das Wohlbefindens sowie Lebensqualität.
Zielgruppe sind überwiegend weibliche Hunde- und Katzenbesitzer mit erkrankten Tieren.
Aufgabenstellung
Flyer sollte klappbar sein. Logo und mein Name und Kontaktdaten sollten enthalten sein.

```html
<!DOCTYPE html>
<html lang="de">
<head>
<meta charset="utf-8">
<title>Flyer – Therapie und Ernährung</title>
<link rel="stylesheet" href="https://fonts.googleapis.com/css2?family=Poppins:wght@400;700&display=swap">
<style>
  :root {
    --mint: #dbf0e4;
    --pale: #f4faf6;
    --ink: #231f35;
    --accent: #d39a62;
    --photo-top: #b9b4ab;
    --photo-bottom: #e9e6e1;
  }
  html, body {
    margin: 0;
    padding: 0;
    width: 1200px;
    height: 2545px;
    overflow: hidden;
    background: var(--pale);
    font-family: "Poppins", sans-serif;
    color: var(--ink);
  }
  .flyer {
    position: relative;
    width: 1200px;
    height: 2545px;
    background: var(--pale);
  }
  .front-panel {
    position: absolute;
    left: 0;
    top: 0;
    width: 1032px;
    height: 2545px;
    background: var(--mint);
  }
  .brand {
    position: absolute;
    left: 121px;
    top: 150px;
    display: flex;
    align-items: center;
    gap: 60px;
  }
  .brand-mark {
    width: 170px;
    height: 170px;
    border-radius: 50%;
    background: var(--accent);
  }
  .brand-name {
    font-weight: 700;
    font-size: 72px;
    line-height: 1;
    color: var(--ink);
  }
  .headline {
    position: absolute;
    left: 121px;
    top: 470px;
    margin: 0;
    font-weight: 700;
    font-size: 127px;
    line-height: 153px;
    letter-spacing: -1px;
  }
  .tagline {
    position: absolute;
    left: 121px;
    top: 1005px;
    margin: 0;
    font-weight: 400;
    font-size: 64px;
    line-height: 89px;
  }
  .portrait {
    position: absolute;
    left: 121px;
    top: 1354px;
    width: 619px;
    height: 698px;
    border-radius: 16px;
    background: linear-gradient(180deg, var(--photo-top) 0%, var(--photo-bottom) 100%);
  }
  .contact {
    position: absolute;
    left: 121px;
    top: 2130px;
    margin: 0;
    font-style: normal;
    font-weight: 400;
    font-size: 57px;
    line-height: 74px;
  }
  .contact .phone { font-weight: 700; }
</style>
</head>
<body>
  <main class="flyer">
    <section class="front-panel">
      <div class="brand">
        <div class="brand-mark"></div>
        <div class="brand-name">Pfotenruhe</div>
      </div>

      <h1 class="headline">Therapie<br>und<br>Ernährung</h1>

      <p class="tagline">Der Weg zu<br>einem besseren<br>Tierleben!</p>

      <div class="portrait" role="img" aria-label="Foto der Tiertherapeutin mit einer weißen Katze auf dem Arm in ihrer Praxis"></div>

      <address class="contact">
        Marlene Haldorf<br>
        <span class="phone">0176-0000 4821</span><br>
        info@pfotenruhe-praxis.de<br>
        www.pfotenruhe-praxis.de
      </address>
    </section>
  </main>
</body>
</html>
```